Kestrel Bridge Consulting (KBC) Business Card Design

I would like to create double-sided business cards that contain:
1) Name: Derek Molvane
2) Phone Number: +1 (555) 218-4907
3) Email: Derek.Molvane@KestrelBridgeConsulting.example
4) Website: KestrelBridgeConsulting.example

I would like to include my logo and a color scheme similar to the Varnholt Grand Prix Ostera squad color scheme (black, silver, greenish-blue – but can also include regular blue)

What we do: Our company develops and delivers innovative and pragmatic information technology and cybersecurity risk and compliance solutions for organizations in the commercial market as well as the federal, and state/local sectors.

```html
<!DOCTYPE html>
<html lang="en">
<head>
<meta charset="utf-8">
<title>Kestrel Bridge Consulting — Business Card</title>
<link rel="stylesheet" href="https://fonts.googleapis.com/css2?family=Exo+2:wght@500&family=Montserrat:wght@400;700&display=swap">
<style>
  :root {
    --backdrop: #d9d6d1;
    --card-light: #ffffff;
    --card-dark: #1d1e1f;
    --ink: #1e1e1e;
    --ink-soft: #333333;
    --teal: #3cb5b4;
    --blue: #1a6fb5;
    --white: #ffffff;
  }
  * { margin: 0; padding: 0; box-sizing: border-box; }
  html, body { width: 900px; height: 1200px; overflow: hidden; }
  body { background: var(--backdrop); position: relative; font-family: "Montserrat", sans-serif; }

  .card {
    position: absolute;
    left: 80px;
    width: 742px;
    height: 440px;
    border-radius: 40px;
    overflow: hidden;
    box-shadow: 0 6px 14px rgba(0,0,0,0.35);
  }
  .card--front { top: 132px; background: var(--card-light); }
  .card--back  { top: 638px; background: var(--card-dark); }

  .brand { position: absolute; display: flex; align-items: center; }
  .brand__mark { border-radius: 50%; background: var(--teal); flex: none; }
  .brand__name {
    font-family: "Exo 2", sans-serif;
    font-weight: 500;
    text-transform: uppercase;
    letter-spacing: 1px;
  }

  .card--front .brand { left: 40px; top: 68px; }
  .card--front .brand__mark { width: 92px; height: 92px; margin-right: 26px; }
  .card--front .brand__name { font-size: 27px; line-height: 28px; color: var(--ink); }

  .card--back .brand { left: 102px; top: 150px; }
  .card--back .brand__mark { width: 150px; height: 150px; margin-right: 36px; }
  .card--back .brand__name { font-size: 38px; line-height: 36px; color: var(--white); }

  .holder { position: absolute; left: 46px; top: 236px; }
  .holder__name { font-size: 24px; font-weight: 700; color: var(--teal); line-height: 30px; }
  .holder__role { font-size: 16px; color: var(--ink-soft); margin-top: 2px; }

  .contacts { position: absolute; left: 46px; top: 312px; list-style: none; }
  .contacts__item { display: flex; align-items: center; height: 22px; color: var(--ink-soft); font-size: 15px; }
  .contacts__item--small { font-size: 14px; }
  .contacts__icon { width: 13px; height: 13px; margin-right: 10px; fill: var(--teal); flex: none; }

  .stripe { position: absolute; left: 0; bottom: 0; width: 742px; height: 20px; }
</style>
</head>
<body>

<section class="card card--front" aria-label="Card front">
  <div class="brand">
    <span class="brand__mark"></span>
    <span class="brand__name">Kestrel<br>Bridge<br>Consulting</span>
  </div>

  <div class="holder">
    <p class="holder__name">Derek Molvane</p>
    <p class="holder__role">Owner</p>
  </div>

  <ul class="contacts">
    <li class="contacts__item">
      <svg class="contacts__icon" viewBox="0 0 16 16"><path d="M3 1h3l1.5 4-2 1.3a9 9 0 0 0 4.2 4.2L11 8.5l4 1.5v3a2 2 0 0 1-2 2A12 12 0 0 1 1 3a2 2 0 0 1 2-2z"/></svg>
      +1 (555) 218-4907
    </li>
    <li class="contacts__item contacts__item--small">
      <svg class="contacts__icon" viewBox="0 0 16 16"><path d="M1 3h14v10H1z M1 3l7 5 7-5" stroke="#fff" stroke-width="1"/></svg>
      Derek.Molvane@KestrelBridgeConsulting.example
    </li>
    <li class="contacts__item">
      <svg class="contacts__icon" viewBox="0 0 16 16"><circle cx="8" cy="8" r="7"/><path d="M1 8h14M8 1c3 3 3 11 0 14M8 1c-3 3-3 11 0 14" stroke="#fff" stroke-width="1" fill="none"/></svg>
      KestrelBridgeConsulting.example
    </li>
  </ul>

  <svg class="stripe" viewBox="0 0 742 20" preserveAspectRatio="none">
    <polygon points="0,2 540,2 526,20 0,20" fill="var(--blue)"/>
    <polygon points="552,2 742,2 742,20 538,20" fill="var(--teal)"/>
  </svg>
</section>

<section class="card card--back" aria-label="Card back">
  <div class="brand">
    <span class="brand__mark"></span>
    <span class="brand__name">Kestrel<br>Bridge<br>Consulting</span>
  </div>
</section>

</body>
</html>
```